Kelmora Business Card

We want a logo that connects with the target consumer who are Retailers in the giftware/wholesale/ecommerce space. We will be constantly changing product lines and industry. We are after a logo that can communicate the meaning of "Kelmora"which means Divine/spiritual/light. The company name and owners are of Indian nationals and want to bring the positivity/growth in the design as a subtle message.
Have attached a logo that we think captures the essence of the word "Kelmora" which is light/glow/divine.

Target Market(s)

Adults based in Australia english speaking aged 20 - 60 years that are in the retail business.

Industry/Entity Type

Business

Font styles to use
Serif
Sans Serif
Decorative
Script

Requirements
Must have
• Logo in form of "D" or "Kelmora" or "Kelmora Pty Ltd"
Nice to have
• I have attached a sample of letter D used as logo. Its shows the glowing sun which is representative/symbolic presentation of word "Kelmora"

```html
<!DOCTYPE html>
<html lang="en">
<head>
<meta charset="utf-8">
<title>Kelmora Business Card</title>
<link rel="stylesheet" href="https://fonts.googleapis.com/css2?family=Crimson+Text:wght@400;600&display=swap">
<style>
  :root {
    --page: #ffffff;
    --border: #000000;
    --front-dark: #353535;
    --front-glow: #ffffff;
    --back-left: #666666;
    --back-right: #999999;
    --ink: #111111;
    --brand: #0b4ea2;
    --sun: #ffcc00;
  }
  * { margin: 0; padding: 0; box-sizing: border-box; }
  html, body {
    width: 897px;
    height: 1200px;
    overflow: hidden;
    background: var(--page);
  }
  body {
    position: relative;
    font-family: "Crimson Text", "Times New Roman", serif;
    color: var(--ink);
  }
  .card {
    position: absolute;
    left: 2px;
    width: 893px;
    height: 524px;
    border: 3px solid var(--border);
    overflow: hidden;
  }
  .card--front {
    top: 2px;
    background: radial-gradient(ellipse 390px 340px at 50% 50%,
      var(--front-glow) 0%, var(--front-glow) 35%, #d9d9d9 72%, var(--front-dark) 100%);
  }
  .card--back {
    top: 674px;
    background: linear-gradient(90deg, var(--back-left) 0%, var(--back-left) 40%, var(--back-right) 100%);
  }
  .brand {
    position: absolute;
    display: flex;
    align-items: center;
    transform: translate(-50%, -50%);
    white-space: nowrap;
  }
  .brand__name {
    font-weight: 600;
    color: var(--brand);
    line-height: 1;
  }
  .brand__dot {
    border-radius: 50%;
    background: var(--sun);
  }
  .card--front .brand { left: 450px; top: 260px; gap: 18px; }
  .card--front .brand__name { font-size: 112px; }
  .card--front .brand__dot { width: 56px; height: 56px; }
  .card--back .brand { left: 727px; top: 82px; gap: 8px; }
  .card--back .brand__name { font-size: 46px; }
  .card--back .brand__dot { width: 22px; height: 22px; }
  .rule {
    position: absolute;
    left: 532px;
    top: 162px;
    width: 362px;
    height: 8px;
    background: linear-gradient(90deg, #ffffff 0%, #7a7a7a 50%, #000000 100%);
  }
  .info {
    position: absolute;
    line-height: 1;
  }
  .info--name { left: 99px; top: 184px; font-size: 27px; }
  .info--company { left: 95px; top: 240px; font-size: 21px; }
  .info--address { left: 95px; top: 363px; font-size: 21px; }
  .info--phone { left: 543px; top: 379px; font-size: 21px; }
  .info--email { left: 543px; top: 422px; font-size: 21px; }
  .info--website { left: 543px; top: 472px; font-size: 21px; }
</style>
</head>
<body>
  <section class="card card--front" aria-label="Card front">
    <div class="brand">
      <span class="brand__dot" aria-hidden="true"></span>
      <span class="brand__name">Kelmora</span>
    </div>
  </section>

  <section class="card card--back" aria-label="Card back">
    <div class="brand">
      <span class="brand__dot" aria-hidden="true"></span>
      <span class="brand__name">Kelmora</span>
    </div>
    <div class="rule" aria-hidden="true"></div>
    <p class="info info--name">Name</p>
    <p class="info info--company">Company</p>
    <p class="info info--address">Address</p>
    <p class="info info--phone">Phone</p>
    <p class="info info--email">Email</p>
    <p class="info info--website">Website</p>
  </section>
</body>
</html>
```